Power Point Template

I would like to have a power point template for our company.
See our website: www.tornvikhamn.se for logo/colors and inspiration.

The template will be used for bank meetings etc, so it should be formal and professional.

Should show examples of various layouts.
Updates

I want the following headings/sections/example slides: - Slide with table of contents - Slide with bullets (just to show how a bullet list looks like) - Slide with project timeline - Slide with business case calculations (table e.g.) - slide with pictures with room for descriptive text (to show inspirational pictures, one slide per section: exterior, interior upper floor, exterior lower floor)? - Slide where our buildings are described (bullet list) - Slide with presentation of our business partners - First page with a faded background picture of our building (the one where our logo is shown)

Industry/Entity Type

It Company

```html
<!DOCTYPE html>
<html lang="en">
<head>
<meta charset="UTF-8">
<title>Amenities</title>
<link href="https://fonts.googleapis.com/css2?family=Oswald:wght@300;400;500;600&display=swap" rel="stylesheet">
<style>
  :root {
    --amber: #f6a623;
    --amber-deep: #ee9a14;
    --navy: #1f3552;
    --sky-top: #5d7ea8;
    --sky-mid: #a7bcd6;
    --sky-low: #d3dde9;
    --road: #6c7a8c;
  }
  * { margin: 0; padding: 0; box-sizing: border-box; }
  html, body { width: 1200px; height: 900px; overflow: hidden; background: #ffffff; }
  .slide {
    position: relative;
    width: 1200px;
    height: 900px;
    overflow: hidden;
    font-family: "Oswald", "Arial Narrow", sans-serif;
    color: var(--navy);
  }
  .street-photo {
    position: absolute;
    left: 582px; top: 0;
    width: 618px; height: 900px;
    background: linear-gradient(180deg, var(--sky-top) 0%, var(--sky-mid) 40%, var(--sky-low) 66%, #9aa6b5 76%, var(--road) 100%);
  }
  .amenities-panel {
    position: absolute;
    left: 0; top: 0;
    width: 582px; height: 900px;
    background: linear-gradient(180deg, var(--amber) 0%, var(--amber-deep) 100%);
  }
  .panel-title {
    position: absolute;
    left: 33px; top: 24px;
    font-size: 42px;
    font-weight: 500;
    line-height: 1;
    transform: scaleX(0.8);
    transform-origin: left top;
    white-space: nowrap;
  }
  .title-rule {
    position: absolute;
    left: 33px; top: 76px;
    width: 336px; height: 5px;
    background: var(--navy);
  }
  .amenity-list { list-style: none; }
  .amenity {
    position: absolute;
    left: 36px;
    top: var(--y);
    display: flex;
    align-items: flex-start;
    gap: 23px;
    font-size: 23px;
    font-weight: 400;
    line-height: 26px;
    width: 540px;
    white-space: nowrap;
  }
  .amenity.two-line { line-height: 31px; }
  .amenity svg { flex: 0 0 22px; width: 22px; height: 22px; margin-top: 2px; }
  .amenity.two-line svg { margin-top: 4px; }
  .brand {
    position: absolute;
    right: 18px; top: 40px;
    display: flex;
    align-items: center;
    gap: 10px;
    font-size: 30px;
    font-weight: 600;
    color: var(--navy);
    letter-spacing: 1px;
  }
  .brand-square { width: 22px; height: 22px; background: var(--navy); }
</style>
</head>
<body>
<div class="slide">
  <div class="street-photo" role="img" aria-label="Photo of an empty industrial street under a cloudy blue sky, with street lamps and low buildings"></div>

  <section class="amenities-panel" role="img" aria-label="Faded photo of a modern building behind an amber overlay">
    <h1 class="panel-title">AMENITIES</h1>
    <div class="title-rule"></div>
    <svg width="0" height="0" style="position:absolute">
      <defs>
        <symbol id="target" viewBox="0 0 24 24">
          <circle cx="12" cy="12" r="10" fill="none" stroke="#1f3552" stroke-width="2.6"/>
          <circle cx="12" cy="12" r="5.5" fill="none" stroke="#1f3552" stroke-width="2.2"/>
          <circle cx="12" cy="12" r="2" fill="#1f3552"/>
        </symbol>
      </defs>
    </svg>
    <ul class="amenity-list">
      <li class="amenity" style="--y:111px"><svg><use href="#target"/></svg><span>24 Hour Valet Services</span></li>
      <li class="amenity" style="--y:158px"><svg><use href="#target"/></svg><span>State Of The Art Health &amp; Fitness Facility</span></li>
      <li class="amenity" style="--y:206px"><svg><use href="#target"/></svg><span>Office Suites For Lease</span></li>
      <li class="amenity" style="--y:252px"><svg><use href="#target"/></svg><span>Micro Convenience Store On Site</span></li>
      <li class="amenity" style="--y:300px"><svg><use href="#target"/></svg><span>Entire Building is "Smart" operated and managed</span></li>
      <li class="amenity" style="--y:348px"><svg><use href="#target"/></svg><span>Tenant Office &amp; Conference Room including;</span></li>
      <li class="amenity" style="--y:389px"><svg><use href="#target"/></svg><span>Computer, wifi, Print, Fax, Scan, Copy Center</span></li>
      <li class="amenity" style="--y:435px"><svg><use href="#target"/></svg><span>Outdoor lounges &amp; fireplaces</span></li>
      <li class="amenity" style="--y:483px"><svg><use href="#target"/></svg><span>Luxury Clubhouse With 73" Smart TV, Patio With</span></li>
      <li class="amenity two-line" style="--y:521px"><svg><use href="#target"/></svg><span>Custom Built Outdoor Pizza Oven and Grill, as well<br>as&nbsp; Hot Tub</span></li>
      <li class="amenity" style="--y:600px"><svg><use href="#target"/></svg><span>Rooftop Landscaped Dog Park and Private</span></li>
      <li class="amenity" style="--y:641px"><svg><use href="#target"/></svg><span>Sanctuary Full of Plants and Flowers.</span></li>
      <li class="amenity" style="--y:689px"><svg><use href="#target"/></svg><span>Wine cellar*</span></li>
      <li class="amenity" style="--y:735px"><svg><use href="#target"/></svg><span>ILounge</span></li>
      <li class="amenity" style="--y:783px"><svg><use href="#target"/></svg><span>Dog Park</span></li>
      <li class="amenity" style="--y:830px"><svg><use href="#target"/></svg><span>Dog wash bay</span></li>
    </ul>
  </section>

  <div class="brand"><span class="brand-square"></span>TORNVIK</div>
</div>
</body>
</html>
```